Junk Removal company with existing WordPress website needs new mobile enhanced website

I am looking to have someone take my existing website and either update it with a new design and menu which is more mobile enhanced (70% of my traffic is from mobile devices and most people stay on the home page to find what they need) or create a new website from scratch to achieve my design goals. My name goal is the have to home page be quick and easy to find what the customer is looking for.
Our current website is: BrightCreekJunkOut.com and plain review badge my business page https://g.page/brightcreekjunkout
I have attached an example the design idea I came up with for the home page based on what I would like it to look like as well as some logo files and pictures.

```html
<!DOCTYPE html>
<html lang="en">
<head>
<meta charset="utf-8">
<title>Bright Creek Junk Out – Junk Hauling &amp; Cleanout</title>
<link href="https://fonts.googleapis.com/css2?family=Montserrat:wght@700;800;900&family=Poppins:wght@400;500;600;700&display=swap" rel="stylesheet">
<style>
:root{
  --orange:#ff8a00;
  --orange-deep:#f06a00;
  --red:#d9410e;
  --ink:#111111;
  --text:#555555;
  --muted:#8a8a8a;
  --grey:#efefef;
  --grey-2:#f6f6f6;
  --dark:#1d1d1d;
  --white:#ffffff;
  --yellow:#ffcc00;
}
*{box-sizing:border-box;margin:0;padding:0}
html,body{width:1200px;height:4695px;overflow:hidden}
body{position:relative;background:var(--white);font-family:'Poppins',sans-serif;color:var(--text);font-size:13px;line-height:1.6}
.abs{position:absolute}
h1,h2,h3{font-family:'Montserrat',sans-serif;color:var(--ink);font-weight:800;text-transform:uppercase}
.hex{clip-path:polygon(25% 4%,75% 4%,100% 50%,75% 96%,25% 96%,0 50%)}
.hex-v{clip-path:polygon(50% 0,96% 25%,96% 75%,50% 100%,4% 75%,4% 25%)}
.btn{display:inline-block;background:var(--orange-deep);color:var(--white);font-family:'Poppins',sans-serif;font-weight:600;font-size:13px;text-transform:uppercase;padding:9px 22px;border-radius:6px}
.brand{display:flex;align-items:center;gap:12px}
.brand-mark{width:40px;height:40px;border-radius:50%;background:var(--orange)}
.brand-name{font-family:'Montserrat',sans-serif;font-weight:800;font-size:18px;line-height:1.05;color:var(--orange);text-transform:uppercase}
.photo{background:linear-gradient(135deg,#8b8f94,#4b4f55)}

/* header */
.topbar{left:600px;top:0;width:600px;height:42px;background:var(--orange);clip-path:polygon(40px 0,100% 0,100% 100%,0 100%);color:var(--white);display:flex;align-items:center;justify-content:flex-end;gap:46px;padding-right:30px;font-size:12px}
.topbar b{font-size:20px;font-weight:600;margin-left:6px}
.header-brand{left:60px;top:20px}
.nav{left:440px;top:62px;display:flex;gap:28px;font-size:12.5px;color:#444}
.nav .active{color:var(--orange-deep);border-left:2px solid var(--orange-deep);padding-left:8px}
.search{left:957px;top:58px;width:34px;height:34px;border:2px solid #333;border-radius:50%}
.header-btn{left:1020px;top:56px}

/* hero */
.hero{left:0;top:105px;width:1200px;height:652px;background:linear-gradient(180deg,#e7e7e7,#f7f7f7);clip-path:polygon(0 0,100% 0,100% 60%,60% 100%,40% 100%,0 60%)}
.hero-photo{left:680px;top:105px;width:520px;height:480px;background:linear-gradient(150deg,#6d7a86,#8a6a4e);clip-path:polygon(0 0,100% 0,100% 45%,60% 100%,30% 100%,0 55%);border-bottom:6px solid var(--orange)}
.hero-frame{left:670px;top:105px;width:540px;height:492px;background:var(--orange);clip-path:polygon(0 0,100% 0,100% 46%,60% 100%,30% 100%,0 56%)}
.hero-title{left:62px;top:232px;font-size:45px;line-height:1.33;font-weight:900}
.hero-title span{color:var(--orange)}
.hero-text{left:62px;top:414px;width:420px;font-size:12px;color:#333}
.hero-btn{left:60px;top:493px}
.dots{left:300px;top:697px;display:flex;align-items:center;gap:10px;font-size:12px;color:#333}
.dots i{display:block;width:40px;height:2px;background:var(--orange)}

/* features */
.features-title{left:0;top:800px;width:1200px;text-align:center;font-size:29px;line-height:1.55}
.feature{width:372px;height:116px;background:var(--white);border-radius:10px;box-shadow:0 4px 18px rgba(0,0,0,.1);padding:22px 22px 0 112px}
.feature .ico{position:absolute;left:18px;top:18px;width:82px;height:82px;background:var(--dark)}
.feature .ico.alt{background:var(--orange)}
.feature .ico svg{position:absolute;left:24px;top:24px}
.feature h4{font-size:14px;font-weight:600;color:var(--ink)}
.feature p{font-size:11.5px;color:var(--muted);margin-top:6px}

/* about */
.about-bg{left:0;top:1210px;width:1200px;height:700px;background:var(--grey);clip-path:polygon(0 100%,0 75%,30% 45%,45% 18%,55% 15%,100% 40%,100% 100%)}
.about-photo-frame{left:88px;top:1270px;width:392px;height:430px;background:var(--orange)}
.about-photo{left:92px;top:1273px;width:380px;height:418px;background:linear-gradient(135deg,#3a3a3a,#c62f24)}
.about-hex-red{left:58px;top:1546px;width:110px;height:120px;background:var(--red)}
.outline-hex{left:1070px;top:1270px}
.about-title{left:556px;top:1270px;font-size:33px}
.about-text{left:556px;top:1320px;width:340px;font-size:12px}
.about-list{left:556px;top:1432px;list-style:none;font-size:12px}
.about-list li{display:flex;align-items:center;gap:18px;height:22.5px}
.about-list li::before{content:"";width:10px;height:10px;border:2px solid var(--orange);border-radius:50%}
.about-btn{left:552px;top:1561px}

/* review band */
.review-title{left:155px;top:1745px;font-size:22px;line-height:1.55;font-weight:800}
.review-sub{left:155px;top:1855px;font-size:12.5px;color:#333}
.review-badge{left:802px;top:1668px;width:205px;height:228px;background:linear-gradient(135deg,var(--orange),var(--red))}
.review-badge-dot{left:868px;top:1745px;width:72px;height:72px;border-radius:50%;background:rgba(255,255,255,.9)}

/* estimate */
.est-bg{left:0;top:1920px;width:1200px;height:520px;background:var(--grey-2);clip-path:polygon(0 0,100% 40%,100% 100%,0 100%)}
.est-bg2{left:0;top:1950px;width:1200px;height:500px;background:var(--white);clip-path:polygon(0 25%,100% 0,100% 100%,0 100%)}
.est-title{left:0;top:1985px;width:1200px;text-align:center;font-size:30px;line-height:1.5}
.est-sub{left:0;top:2072px;width:1200px;text-align:center;font-size:13px;font-weight:500;color:#555}
.est-sub2{left:0;top:2094px;width:1200px;text-align:center;font-size:12.5px;font-weight:600;color:var(--red)}
.way{width:300px}
.way .badge{width:150px;height:165px;position:relative;filter:drop-shadow(0 3px 6px rgba(0,0,0,.15))}
.way .badge .shell{position:absolute;inset:0;background:var(--white)}
.way .badge .core{position:absolute;left:8px;top:9px;width:134px;height:147px}
.way .badge svg{position:absolute;left:45px;top:52px}
.way h4{margin-top:30px;font-size:13px;font-weight:600;color:var(--ink)}
.way p{font-size:11.5px;color:var(--muted);margin-top:4px;width:210px}

/* pricing trucks */
.trucks-title{left:62px;top:2455px;font-size:30px}
.trucks-text{left:62px;top:2497px;width:520px;font-size:11.5px;color:#444}
.truck{width:120px;height:64px}
.truck .body{position:absolute;left:0;top:6px;width:82px;height:48px;border-radius:3px}
.truck .cab{position:absolute;left:86px;top:18px;width:34px;height:36px;background:#d7dde2;border-radius:3px 10px 3px 3px}
.truck .w{position:absolute;top:48px;width:16px;height:16px;border-radius:50%;background:#222}
.truck-stats{font-size:12.5px;font-weight:600;color:#444;line-height:30px}
.trucks-photo-frame{left:810px;top:2462px;width:334px;height:340px;background:var(--orange)}
.trucks-photo{left:816px;top:2468px;width:322px;height:328px;background:linear-gradient(160deg,#b6bcc2,#53585e)}
.trucks-hex{left:802px;top:2658px;width:80px;height:90px;background:var(--red)}

/* services */
.services-title{left:128px;top:2817px;font-size:30px}
.svc{width:290px;height:421px;background:var(--white);box-shadow:0 4px 18px rgba(0,0,0,.12);border-radius:0 0 6px 6px}
.svc .pic{position:absolute;left:0;top:0;width:290px;height:208px;clip-path:polygon(0 0,100% 0,100% 100%,40% 100%,0 80%)}
.svc.hl{background:var(--orange)}
.svc h4{position:absolute;left:18px;top:222px;font-size:16px;font-weight:600;color:var(--ink)}
.svc.hl h4,.svc.hl li,.svc.hl .more{color:var(--white)}
.svc ul{position:absolute;left:18px;top:256px;list-style:none;font-size:12px}
.svc li{display:flex;align-items:center;gap:10px;height:22.7px}
.svc li svg{flex:none}
.svc .more{position:absolute;left:18px;top:385px;font-size:11px;font-weight:700;color:var(--red);text-decoration:underline}

/* cta */
.cta-bg{left:0;top:3330px;width:1200px;height:360px;background:var(--grey);clip-path:polygon(0 100%,0 40%,35% 20%,100% 30%,100% 60%,60% 85%)}
.cta-frame{left:58px;top:3345px;width:276px;height:305px;background:var(--orange)}
.cta-photo{left:63px;top:3350px;width:266px;height:295px;background:linear-gradient(160deg,#7d8a97,#2f3f66)}
.cta-title{left:392px;top:3355px;width:620px;font-size:23px;line-height:1.6}
.cta-btn{left:390px;top:3513px}

/* how we price */
.price-title{left:0;top:3655px;width:1200px;text-align:center;font-size:30px}
.price-item{width:250px}
.price-item .pi{width:64px;height:52px;position:relative}
.price-item .pi span{position:absolute;left:0;top:0;width:40px;height:44px;background:#fde0cc;border-radius:4px}
.price-item .pi b{position:absolute;left:28px;top:20px;width:28px;height:28px;border:2px solid var(--red);border-radius:50%;background:var(--white)}
.price-item h4{font-size:13.5px;font-weight:600;color:var(--ink);margin-top:10px}
.price-item p{font-size:11.5px;color:var(--muted);margin-top:8px;line-height:1.7}

/* service area */
.area-deco{left:0;top:4010px;width:1200px;height:340px;background:var(--red);clip-path:polygon(100% 0,100% 100%,60% 100%)}
.area-deco2{left:0;top:4010px;width:1200px;height:340px;background:var(--orange);clip-path:polygon(100% 8%,100% 100%,66% 100%)}
.area-title{left:62px;top:4108px;font-size:33px}
.area-list{list-style:none;font-size:13px;font-weight:600;color:#222}
.area-list li{display:flex;align-items:center;gap:14px;height:30.5px}
.area-list li::before{content:"";width:12px;height:12px;border:2px solid var(--orange);border-radius:50%}

/* footer */
.footer{left:0;top:4341px;width:1200px;height:320px;background:var(--dark)}
.foot-brand{left:62px;top:4375px}
.foot-brand .brand-name{font-size:22px}
.foot-brand .brand-mark{width:60px;height:60px}
.foot-text{left:62px;top:4490px;width:230px;font-size:11.5px;color:#d8d8d8}
.foot-head{font-family:'Poppins',sans-serif;font-size:18px;font-weight:600;color:var(--orange)}
.foot-links{list-style:none;font-size:11.5px;color:#cfcfcf;margin-top:12px}
.foot-links li{height:27px}
.tree-frame{left:758px;top:4075px;width:326px;height:360px;background:var(--orange)}
.tree-photo{left:766px;top:4082px;width:310px;height:346px;background:linear-gradient(170deg,#8da0ae,#6d5a3e)}
.contact-head{left:766px;top:4452px;width:310px;text-align:center;font-size:18px;font-weight:600;color:var(--orange);line-height:1.55}
.contact-btn{left:860px;top:4522px;font-size:14px;padding:6px 22px}
.copy{left:0;top:4660px;width:1200px;height:35px;background:var(--red);color:#ffe6d9;font-size:11.5px;text-align:center;line-height:35px}
</style>
</head>
<body>

<!-- header -->
<div class="abs topbar"><span>Mon to Sat – 8AM to 6PM</span><span>Call Us : <b>(555) 014-0827</b></span></div>
<div class="abs brand header-brand"><span class="brand-mark"></span><span class="brand-name">Bright Creek<br>Junk Out</span></div>
<nav class="abs nav"><span class="active">Home</span><span>Our Services</span><span>What We Take</span><span>Service Areas</span><span>Contact Us</span></nav>
<div class="abs search"><svg width="30" height="30" viewBox="0 0 30 30"><circle cx="14" cy="14" r="5" fill="none" stroke="#333" stroke-width="2"/><line x1="18" y1="18" x2="21" y2="21" stroke="#333" stroke-width="2"/></svg></div>
<span class="abs btn header-btn">Contct Us</span>

<!-- hero -->
<section class="abs hero" role="img" aria-label="Faded background of a junk removal truck at a house"></section>
<div class="abs hero-frame"></div>
<div class="abs hero-photo" role="img" aria-label="Worker loading an old hot tub onto a truck"></div>
<h1 class="abs hero-title">The best rated junk<br>hauling <span>and cleanout</span><br><span>service</span></h1>
<p class="abs hero-text">Bright Creek Junk Out is a family owned &amp; operated local business offering junk removal, property cleanouts, light demolition and dumpster rental services.</p>
<span class="abs btn hero-btn">Contct Us</span>
<div class="abs dots"><i></i><b>01</b><b>02</b><span style="color:#aaa">03</span></div>

<!-- features -->
<h2 class="abs features-title">Bright Creek's most<br>professional junk removal service</h2>
<div class="abs feature" style="left:210px;top:921px"><div class="ico hex-v"><svg width="34" height="34" viewBox="0 0 34 34" fill="none" stroke="#ff8a00" stroke-width="2"><rect x="4" y="7" width="26" height="23" rx="2"/><line x1="4" y1="13" x2="30" y2="13"/><line x1="11" y1="3" x2="11" y2="9"/><line x1="23" y1="3" x2="23" y2="9"/></svg></div><h4>Easy Scheduling</h4><p>Just give us a call, text or contact<br>us by email!</p></div>
<div class="abs feature" style="left:620px;top:921px"><div class="ico hex-v"><svg width="34" height="34" viewBox="0 0 34 34" fill="none" stroke="#ff8a00" stroke-width="2"><rect x="2" y="10" width="20" height="14"/><path d="M22 14h6l4 5v5h-10z"/><circle cx="9" cy="27" r="3"/><circle cx="26" cy="27" r="3"/></svg></div><h4>All Cleaned Up</h4><p>When we're finishing up, we'll<br>check to make sure we .</p></div>
<div class="abs feature" style="left:210px;top:1047px"><div class="ico hex-v"><svg width="34" height="34" viewBox="0 0 34 34" fill="none" stroke="#ff8a00" stroke-width="2"><path d="M4 17l13-13h13v13l-13 13z"/><circle cx="23" cy="11" r="2.5"/></svg></div><h4>Upfront Pricing</h4><p>When we get there, just show us<br>what you want us to take.</p></div>
<div class="abs feature" style="left:620px;top:1047px"><div class="ico alt hex-v"><svg width="34" height="34" viewBox="0 0 34 34" fill="none" stroke="#fff" stroke-width="2"><circle cx="17" cy="17" r="12"/><ellipse cx="17" cy="17" rx="5" ry="12"/><line x1="5" y1="17" x2="29" y2="17"/></svg></div><h4>Excellent Communication</h4><p>Our Team will always keep you in<br>the loop.</p></div>

<!-- about -->
<div class="abs about-bg"></div>
<div class="abs about-photo-frame hex"></div>
<div class="abs about-photo hex" role="img" aria-label="Crew members in red jackets carrying a sofa into a truck"></div>
<div class="abs about-hex-red hex-v"></div>
<svg class="abs outline-hex" width="130" height="190" viewBox="0 0 130 190"><polygon points="65,2 128,40 128,150 65,188 2,150 2,40" fill="none" stroke="var(--red)" stroke-width="1.5"/></svg>
<h2 class="abs about-title">About Us</h2>
<p class="abs about-text">Bright Creek Junk Out is a family owned &amp; operated local business offering junk removal, property cleanouts, light demolition and dumpster rental services.&nbsp; Local, Professional, Affordable and Dependable.</p>
<ul class="abs about-list"><li>Junk Removal</li><li>Property Cleanout</li><li>Light Demolition</li><li>Dumpster Rental</li><li>Property Cleanouts</li></ul>
<span class="abs btn about-btn">Contct Us</span>

<!-- review band -->
<h2 class="abs review-title">Best rated junk removal &amp; property<br>cleanout company ine the Bright<br>Creek</h2>
<p class="abs review-sub">Fast,Friendly &amp; Professional ......</p>
<div class="abs review-badge hex-v"></div>
<div class="abs review-badge-dot"></div>

<!-- estimate -->
<div class="abs est-bg"></div>
<div class="abs est-bg2"></div>
<h2 class="abs est-title">3 simple ways to get your<br>estimate today !</h2>
<p class="abs est-sub">We Make the Process</p>
<p class="abs est-sub2">QUICK &amp; EASY</p>
<div class="abs way" style="left:241px;top:2148px"><div class="badge"><div class="shell hex-v"></div><div class="core hex-v" style="background:var(--orange-deep)"></div><svg width="60" height="60" viewBox="0 0 24 24"><path fill="#fff" d="M6.6 10.8a15 15 0 0 0 6.6 6.6l2.2-2.2c.3-.3.7-.4 1-.2 1.1.4 2.3.6 3.6.6.6 0 1 .4 1 1V20c0 .6-.4 1-1 1A17 17 0 0 1 3 4c0-.6.4-1 1-1h3.5c.6 0 1 .4 1 1 0 1.3.2 2.5.6 3.6.1.3 0 .7-.2 1z"/></svg></div><h4>Click To CALL</h4><p>CALL US today and talk to one of our friendly,local staff members.</p></div>
<div class="abs way" style="left:534px;top:2148px"><div class="badge"><div class="shell hex-v"></div><div class="core hex-v" style="background:var(--red)"></div><svg width="60" height="60" viewBox="0 0 60 60"><rect x="12" y="6" width="34" height="46" fill="#fff"/><rect x="17" y="12" width="24" height="4" fill="#d9410e"/><g stroke="#d9410e" stroke-width="2"><line x1="17" y1="24" x2="41" y2="24"/><line x1="17" y1="30" x2="41" y2="30"/><line x1="17" y1="36" x2="41" y2="36"/><line x1="17" y1="42" x2="35" y2="42"/></g></svg></div><h4>Click To TEXT</h4><p>TEXT US today with photos of the stuff you would like removed.</p></div>
<div class="abs way" style="left:812px;top:2148px"><div class="badge"><div class="shell hex-v"></div><div class="core hex-v" style="background:var(--yellow)"></div><svg width="60" height="60" viewBox="0 0 60 60"><rect x="4" y="12" width="52" height="36" fill="#fff"/><path d="M6 14l24 20 24-20" fill="none" stroke="#ffcc00" stroke-width="4"/></svg></div><h4>Click To EMAIL</h4><p>EMAIL US today what you would like us to haul away.</p></div>

<!-- bigger truck pricing -->
<h2 class="abs trucks-title">Bigger truck,butter pricing !</h2>
<p class="abs trucks-text">Bright Creek Junk Out is a local family owned &amp; operated business and not a large national franchise. that means we don't have to pass along the 10-12% franchise fee on to our customers like our competitors.</p>
<div class="abs truck" style="left:60px;top:2585px" role="img" aria-label="Our junk removal truck"><div class="body" style="background:#2b2b2b"></div><div class="cab"></div><i class="w" style="left:16px"></i><i class="w" style="left:92px"></i></div>
<div class="abs truck" style="left:300px;top:2585px" role="img" aria-label="Competitor truck"><div class="body" style="background:#d32a1e"></div><div class="cab"></div><i class="w" style="left:16px"></i><i class="w" style="left:92px"></i></div>
<div class="abs truck" style="left:526px;top:2585px" role="img" aria-label="Competitor truck"><div class="body" style="background:#2b3a9a"></div><div class="cab"></div><i class="w" style="left:16px"></i><i class="w" style="left:92px"></i></div>
<div class="abs truck-stats" style="left:62px;top:2665px">7 pickup loads<br>560 cubic feet<br>21 cubic yards</div>
<div class="abs truck-stats" style="left:308px;top:2665px">6 pickup loads<br>480 cubic feet<br>18 cubic yards</div>
<div class="abs truck-stats" style="left:534px;top:2665px">5 pickup loads<br>400 cubic yards<br>15 cubic yards</div>
<div class="abs trucks-photo-frame hex-v"></div>
<div class="abs trucks-photo hex-v" role="img" aria-label="Rear view of a junk removal truck with a worker"></div>
<div class="abs trucks-hex hex-v"></div>

<!-- services -->
<h2 class="abs services-title">Our Services</h2>
<div class="abs svc" style="left:126px;top:2869px"><div class="pic" style="background:linear-gradient(150deg,#9aa0a6,#b8312a)" role="img" aria-label="Truck loaded with household junk"></div><h4>Junk Removal</h4>
<ul><li><svg width="14" height="14" viewBox="0 0 14 14"><circle cx="7" cy="7" r="6" fill="none" stroke="#f06a00" stroke-width="1.5"/><path d="M4 7l2 2 4-4" fill="none" stroke="#f06a00" stroke-width="1.5"/></svg>Misc.Household Junk</li><li><svg width="14" height="14" viewBox="0 0 14 14"><circle cx="7" cy="7" r="6" fill="none" stroke="#f06a00" stroke-width="1.5"/><path d="M4 7l2 2 4-4" fill="none" stroke="#f06a00" stroke-width="1.5"/></svg>Furniture Removal</li><li><svg width="14" height="14" viewBox="0 0 14 14"><circle cx="7" cy="7" r="6" fill="none" stroke="#f06a00" stroke-width="1.5"/><path d="M4 7l2 2 4-4" fill="none" stroke="#f06a00" stroke-width="1.5"/></svg>Mattress Removal</li><li><svg width="14" height="14" viewBox="0 0 14 14"><circle cx="7" cy="7" r="6" fill="none" stroke="#f06a00" stroke-width="1.5"/><path d="M4 7l2 2 4-4" fill="none" stroke="#f06a00" stroke-width="1.5"/></svg>Hot Tub Removal</li><li><svg width="14" height="14" viewBox="0 0 14 14"><circle cx="7" cy="7" r="6" fill="none" stroke="#f06a00" stroke-width="1.5"/><path d="M4 7l2 2 4-4" fill="none" stroke="#f06a00" stroke-width="1.5"/></svg>Yard Debris Removal</li></ul><span class="more">READ MORE</span></div>
<div class="abs svc hl" style="left:454px;top:2869px"><div class="pic" style="background:linear-gradient(150deg,#4d5a45,#2c3328)" role="img" aria-label="Crew clearing demolition debris in a yard"></div><h4>Light Demolition &amp; Tear Down</h4>
<ul><li><svg width="14" height="14" viewBox="0 0 14 14"><circle cx="7" cy="7" r="6" fill="none" stroke="#fff" stroke-width="1.5"/><path d="M4 7l2 2 4-4" fill="none" stroke="#fff" stroke-width="1.5"/></svg>Shed Removal</li><li><svg width="14" height="14" viewBox="0 0 14 14"><circle cx="7" cy="7" r="6" fill="none" stroke="#fff" stroke-width="1.5"/><path d="M4 7l2 2 4-4" fill="none" stroke="#fff" stroke-width="1.5"/></svg>Fence Removal</li><li><svg width="14" height="14" viewBox="0 0 14 14"><circle cx="7" cy="7" r="6" fill="none" stroke="#fff" stroke-width="1.5"/><path d="M4 7l2 2 4-4" fill="none" stroke="#fff" stroke-width="1.5"/></svg>Deck Removal</li><li><svg width="14" height="14" viewBox="0 0 14 14"><circle cx="7" cy="7" r="6" fill="none" stroke="#fff" stroke-width="1.5"/><path d="M4 7l2 2 4-4" fill="none" stroke="#fff" stroke-width="1.5"/></svg>Hot Tub Removal</li><li><svg width="14" height="14" viewBox="0 0 14 14"><circle cx="7" cy="7" r="6" fill="none" stroke="#fff" stroke-width="1.5"/><path d="M4 7l2 2 4-4" fill="none" stroke="#fff" stroke-width="1.5"/></svg>Play Structure Removal</li></ul><span class="more">READ MORE</span></div>
<div class="abs svc" style="left:784px;top:2869px"><div class="pic" style="background:linear-gradient(150deg,#a0a6ac,#3d5d8c)" role="img" aria-label="House yard piled with items from a property cleanout"></div><h4>Property Cleanouts</h4>
<ul><li><svg width="14" height="14" viewBox="0 0 14 14"><circle cx="7" cy="7" r="6" fill="none" stroke="#f06a00" stroke-width="1.5"/><path d="M4 7l2 2 4-4" fill="none" stroke="#f06a00" stroke-width="1.5"/></svg>Estate Cleanout</li><li><svg width="14" height="14" viewBox="0 0 14 14"><circle cx="7" cy="7" r="6" fill="none" stroke="#f06a00" stroke-width="1.5"/><path d="M4 7l2 2 4-4" fill="none" stroke="#f06a00" stroke-width="1.5"/></svg>Residential Cleanout</li><li><svg width="14" height="14" viewBox="0 0 14 14"><circle cx="7" cy="7" r="6" fill="none" stroke="#f06a00" stroke-width="1.5"/><path d="M4 7l2 2 4-4" fill="none" stroke="#f06a00" stroke-width="1.5"/></svg>Garage Cleanout</li><li><svg width="14" height="14" viewBox="0 0 14 14"><circle cx="7" cy="7" r="6" fill="none" stroke="#f06a00" stroke-width="1.5"/><path d="M4 7l2 2 4-4" fill="none" stroke="#f06a00" stroke-width="1.5"/></svg>Storage Unit Clenout</li><li><svg width="14" height="14" viewBox="0 0 14 14"><circle cx="7" cy="7" r="6" fill="none" stroke="#f06a00" stroke-width="1.5"/><path d="M4 7l2 2 4-4" fill="none" stroke="#f06a00" stroke-width="1.5"/></svg>Attic Clean Out</li></ul><span class="more">READ MORE</span></div>

<!-- cta -->
<div class="abs cta-bg"></div>
<div class="abs cta-frame hex"></div>
<div class="abs cta-photo hex" role="img" aria-label="Loaded junk removal truck parked in front of a house"></div>
<h2 class="abs cta-title">Our professional &amp; friendly junk removal experts you call, we haul! we'll solve all your junk removal &amp; property cleanout problems.</h2>
<span class="abs btn cta-btn">Book Your Service</span>

<!-- how we price -->
<h2 class="abs price-title">How we price</h2>
<div class="abs price-item" style="left:62px;top:3739px"><div class="pi"><span></span><b></b></div><h4>Volume Based Pricing</h4><p>Our pricing is based on the amount of space your items take up in our truck.</p></div>
<div class="abs price-item" style="left:337px;top:3739px"><div class="pi"><span></span><b></b></div><h4>Minimun Loads</h4><p>Our pricing is starts at a minimum pickup fee and goes up though twelve different price points to a full load rate.</p></div>
<div class="abs price-item" style="left:613px;top:3739px"><div class="pi"><span></span><b></b></div><h4>Free Estimates</h4><p>We can provide a free estimate over the phone,text or email so you know a price range before we show up.</p></div>
<div class="abs price-item" style="left:888px;top:3739px"><div class="pi"><span></span><b></b></div><h4>Upfront Pricing</h4><p>We always provide our valued customers with a firm price on-site before we beging a job.</p></div>

<!-- service area -->
<div class="abs area-deco"></div>
<div class="abs area-deco2"></div>
<h2 class="abs area-title">Service Area</h2>
<ul class="abs area-list" style="left:62px;top:4150px"><li>Boise</li><li>Meridian</li><li>Eagle</li><li>Star</li><li>Nampa</li></ul>
<ul class="abs area-list" style="left:240px;top:4150px"><li>Caldwell</li><li>Middleton</li><li>Garden city</li><li>Kuna</li><li>Emmett</li></ul>

<!-- footer -->
<footer class="abs footer"></footer>
<div class="abs tree-frame hex-v"></div>
<div class="abs tree-photo hex-v" role="img" aria-label="Worker cutting a large fallen tree trunk beside a house"></div>
<div class="abs brand foot-brand"><span class="brand-mark"></span><span class="brand-name">Bright Creek<br>Junk Out</span></div>
<p class="abs foot-text">Bright Creek Junk Out is a family owned &amp; operated local business offering junk removal, property cleanouts, light demolition and dumpster rental services.</p>
<div class="abs" style="left:338px;top:4385px"><div class="foot-head">Site Map</div><ul class="foot-links"><li>- Home</li><li>- About Us</li><li>- What We Take</li><li>- Service</li><li>- Services Area</li><li>- Reviews</li><li>- Contact Us</li></ul></div>
<div class="abs" style="left:613px;top:4385px"><div class="foot-head">Services</div><ul class="foot-links"><li>- Junk Removal &amp; Hauling</li><li>- Property Cleanout</li><li>- Light Demolition</li><li>- Dumpster Rental</li></ul></div>
<div class="abs contact-head">Contact Bright Creek<br>Junk Out</div>
<span class="abs btn contact-btn">(555) 014-0827</span>
<div class="abs copy">© 2021 Bright Creek Junk Out. All Rights Reserved.</div>

</body>
</html>
```